Billboard design 8x3M NURA (Spanish company)

We´re located in the south of Spain. We run a local telecom company.
We sell Fiber optic, and mobile phone lines mainly.
The billboard will have to be in Spanish, I would like the price to be something you spot on first sight when passing by in the car.
Our company color is blue, like in our logo which I will add. I will also add a example from what we currently have.
The new offer should be:
1000 megas + 100Gigas movil con llamadas ilimitadas. (meaning 1000Mb fiber optic speed and 100Gb data and unlimited calls for 1 mobile line)
Our details are: phone line 952 00 0147
Website: nu-ra.es

```html
<!DOCTYPE html>
<html lang="es">
<head>
<meta charset="utf-8">
<title>NURA – Valla 8x3</title>
<link href="https://fonts.googleapis.com/css2?family=Exo+2:wght@600;700;800&family=Saira+Condensed:wght@600;700&display=swap" rel="stylesheet">
<style>
  :root {
    --navy: #0b4f82;
    --cyan: #1cc0f2;
    --cyan-dash: #2cb6ea;
    --white: #ffffff;
    --stage: #e8edf1;
    --photo-a: #e4ecf1;
    --photo-b: #c8d5dd;
    --photo-c: #b9c6cf;
  }
  * { margin: 0; padding: 0; box-sizing: border-box; }
  html, body { width: 1200px; height: 874px; overflow: hidden; }
  body { background: var(--stage); position: relative; font-family: "Exo 2", sans-serif; }

  .billboard {
    position: absolute; left: 20px; top: 227px;
    width: 1160px; height: 420px;
    background: var(--white); overflow: hidden;
  }
  .hero-photo {
    position: absolute; left: 540px; top: 0; width: 620px; height: 420px;
    background: linear-gradient(90deg, var(--white) 0%, var(--photo-a) 22%, var(--photo-b) 55%, var(--photo-c) 80%, var(--photo-a) 100%);
  }
  .shapes { position: absolute; left: 0; top: 0; }

  .price { position: absolute; left: 135px; top: 14px; width: 306px; text-align: center; color: var(--white); }
  .price-amount { font-weight: 800; font-size: 96px; line-height: 1; letter-spacing: -3px; }
  .price-note { font-weight: 700; font-size: 23px; margin-top: 8px; }

  .brand { position: absolute; left: 532px; top: 18px; }
  .brand-name { font-weight: 800; font-size: 70px; line-height: 1; color: var(--cyan); letter-spacing: 4px; }
  .brand-services { font-weight: 700; font-size: 20px; color: var(--cyan); margin-top: 8px; }
  .brand-services .sep { margin: 0 6px; }
  .brand-services .dark { color: var(--navy); }

  .offer {
    position: absolute; left: 36px; top: 217px; width: 544px; height: 62px;
    background: var(--navy); border-radius: 10px;
    color: var(--white); font-family: "Saira Condensed", sans-serif; font-weight: 700;
    font-size: 52px; line-height: 62px; text-align: center; letter-spacing: 0.5px;
  }
  .offer-sub {
    position: absolute; left: 88px; top: 282px;
    font-family: "Saira Condensed", sans-serif; font-weight: 700; font-size: 28px;
    color: var(--navy); letter-spacing: 0.3px;
  }

  .contact { position: absolute; left: 28px; top: 346px; display: flex; align-items: center; color: var(--white); }
  .contact-icon { width: 42px; height: 42px; border-radius: 50%; background: var(--navy); display: flex; align-items: center; justify-content: center; }
  .contact-text { font-weight: 700; font-size: 50px; line-height: 1; margin-left: 12px; margin-right: 14px; }
  .contact-web { letter-spacing: -0.5px; }
</style>
</head>
<body>
  <div class="billboard">
    <div class="hero-photo" role="img" aria-label="Hombre joven con camiseta blanca mirando su móvil junto a un portátil, con un icono de wifi de fondo"></div>

    <svg class="shapes" width="1160" height="420" viewBox="0 0 1160 420">
      <circle cx="288" cy="36" r="164" fill="none" stroke="var(--cyan-dash)" stroke-width="2" stroke-dasharray="8 6"/>
      <circle cx="288" cy="36" r="153" fill="var(--navy)"/>
      <path d="M0 332 L690 328 C760 326 785 346 815 366 C845 384 875 384 920 383 L1160 380 L1160 420 L0 420 Z" fill="var(--cyan)"/>
      <path d="M690 322 C765 320 790 342 820 360 C850 377 880 378 920 377 L1160 374" fill="none" stroke="var(--white)" stroke-width="6"/>
    </svg>

    <div class="price">
      <div class="price-amount">35€</div>
      <div class="price-note">Por sólo</div>
    </div>

    <div class="brand">
      <div class="brand-name">NURA</div>
      <div class="brand-services">Wifi<span class="sep">|</span>Fibra<span class="sep">|</span><span class="dark">Movil<span class="sep">|</span>Tv</span></div>
    </div>

    <div class="offer">1000 MEGAS + 100GIGAS</div>
    <div class="offer-sub">MOVIL CON LLAMADAS ILIMITADAS</div>

    <div class="contact">
      <span class="contact-icon">
        <svg width="22" height="22" viewBox="0 0 24 24"><path fill="#fff" d="M6.6 10.8a15.1 15.1 0 0 0 6.6 6.6l2.2-2.2a1 1 0 0 1 1-.25 11.4 11.4 0 0 0 3.6.57 1 1 0 0 1 1 1V20a1 1 0 0 1-1 1A17 17 0 0 1 3 4a1 1 0 0 1 1-1h3.5a1 1 0 0 1 1 1c0 1.25.2 2.45.57 3.57a1 1 0 0 1-.25 1z"/></svg>
      </span>
      <span class="contact-text">952 00 0147</span>
      <span class="contact-icon">
        <svg width="22" height="22" viewBox="0 0 24 24"><rect x="5" y="5" width="14" height="10" rx="1" fill="none" stroke="#fff" stroke-width="2"/><rect x="2" y="17" width="20" height="2" rx="1" fill="#fff"/></svg>
      </span>
      <span class="contact-text contact-web">nu-ra.es</span>
    </div>
  </div>
</body>
</html>
```